Value of Working with an Agent

We need a flyer design in standard 8.5x11 format. One side full-color design. I am an agent and will be using this flyer to promote to Skilled Nursing Centers on the Value of working with an insurance agent. I'm looking for an eye-catching flyer that draws the readers attention to the value added services I provide.

Images of the services from their respective companies are provided.
The two focus products providing the services are: 1)Golden Horizons and 2)LWBQ Medicare Harbor.

Look and Feel:
Elegant, Professional, Colorful, Eye-Catching

Target Market:
Skilled Nursing Home Managers

Target Market(s)

Industry/Entity Type

Medicare

Font styles to use
Serif

Requirements
Must have
• Content:
• -Medicare only clients can get upgraded benefits with an MAPD plan
• -High rated MAPD plans result in Higher Capitation rates for Skilled Nursing Homes
• -MAPD plans come with CareBeacon to help lower-income Medicare patients get help through 2,000 different community assistant programs.
• -All paperwork is handled by the agent. Usually done in 30 mins and patients plans start the very next month.
• -All Medicare patients entering a Skilled Nursing Center are eligible to make any changes needed to their Medicare benefits upon entering the Skilled Nursing Facility.
• -MAPD plans offer a personal case manager for their patients when they leave the Skilled Nursing Home.
• -Patients Benefits included in our MAPD plans: 24hr Nurse Hotline, $200 per year credit for Over-the-Counter items, Chiropractic and Acupuncture Coverage, $0 copay Eye Exams, 2 Dental Cleanings per year. Virtual Doctor Visits, House Call Coverage, $0 monthly premium.
• -Services provided by me are no cost to both the Nursing Home and the patient.
• -Agent information: Name: Brent Valdecour Phone: (702)555-0187 Email: b.valdecour@pinemarkcover.example
• Images of the services from their respective companies are provided.
• The two focus products providing the services are: 1)Golden Horizons and 2)LWBQ Medicare Harbor.

```html
<!DOCTYPE html>
<html lang="en">
<head>
<meta charset="utf-8">
<title>The Value of Working With An Insurance Agent</title>
<link href="https://fonts.googleapis.com/css2?family=Raleway:wght@300;400;500;600;700;800&display=swap" rel="stylesheet">
<style>
  :root{
    --page-bg:#c9c9cb;
    --navy:#0b3f78;
    --navy-deep:#083263;
    --cyan:#14a5e6;
    --tick:#2aa8ee;
    --white:#ffffff;
    --ink-blue:#1a4f8c;
    --rule:#9aa7b6;
    --photo-light:#e9eef3;
    --photo-mid:#bcd2e4;
  }
  *{margin:0;padding:0;box-sizing:border-box}
  html,body{width:1200px;height:1200px;overflow:hidden;background:var(--page-bg);font-family:'Raleway',sans-serif}
  .flyer{
    position:absolute;left:152px;top:20px;width:998px;height:1292px;
    background:var(--white);transform:scale(0.898);transform-origin:0 0;overflow:hidden;
  }
  .hero-photo{
    position:absolute;left:0;top:0;width:998px;height:440px;
    background:linear-gradient(160deg,var(--photo-light) 0%,#dbe6ef 45%,var(--photo-mid) 100%);
  }
  .blue-field{position:absolute;left:0;top:0;width:998px;height:1292px}
  .benefits-card{
    position:absolute;left:61px;top:212px;width:344px;height:221px;border-radius:10px;
    border:2px solid #1b1b1b;background:linear-gradient(180deg,#f5f5f5,#e3e6ea);
  }
  .headline{position:absolute;left:59px;top:448px;color:var(--white);font-size:70px;line-height:72px;letter-spacing:-1.5px;font-weight:300;white-space:nowrap}
  .headline strong{font-weight:800}
  .checklist{position:absolute;top:604px;width:400px;list-style:none;color:var(--white)}
  .checklist.left{left:59px}
  .checklist.right{left:519px;width:420px}
  .checklist li{position:relative;padding-left:34px;font-size:17.5px;line-height:23px;font-weight:300;margin-bottom:13px}
  .checklist li svg{position:absolute;left:0;top:2px;width:24px;height:24px}
  .section-bar{position:absolute;left:0;top:851px;width:52px;height:33px;background:var(--cyan)}
  .section-title{position:absolute;left:59px;top:848px;font-size:32px;font-weight:600;color:var(--white);letter-spacing:-0.5px;white-space:nowrap}
  .section-cap{position:absolute;left:357px;top:851px;width:18px;height:33px;background:var(--cyan)}
  .benefits-intro{position:absolute;left:59px;top:895px;font-size:21px;font-weight:600;color:var(--white);white-space:nowrap}
  .benefit-list{position:absolute;top:926px;list-style:none;color:var(--white);font-size:19px;font-weight:600;line-height:28.5px;white-space:nowrap}
  .benefit-list.left{left:59px}
  .benefit-list.right{left:366px}
  .benefit-list li{position:relative;padding-left:23px}
  .benefit-list li::before{content:"•";position:absolute;left:0;font-size:14px}
  .agent-portrait{
    position:absolute;left:682px;top:858px;width:256px;height:256px;border-radius:50%;
    background:radial-gradient(circle at 45% 40%,#d9c2ae 0%,#a58a77 45%,#5a5a66 100%);
  }
  .partner-name{position:absolute;font-weight:600;color:var(--ink-blue);white-space:nowrap}
  .partner-rule{position:absolute;left:59px;top:1195px;width:485px;height:1px;background:var(--rule)}
  .partner-row{
    position:absolute;left:59px;top:1212px;width:485px;display:flex;justify-content:space-between;align-items:center;
  }
  .partner-row .partner{font-size:15px;font-weight:600;color:var(--ink-blue);white-space:nowrap;display:flex;align-items:center}
  .partner-row .dot{display:inline-block;width:13px;height:13px;border-radius:50%;background:var(--ink-blue);margin-right:6px;flex:none}
  .contact{position:absolute;right:59px;text-align:right;color:var(--ink-blue);white-space:nowrap}
  .contact-name{top:1128px;font-size:34px;font-weight:600}
  .contact-phone{top:1170px;font-size:38px;font-weight:700;display:flex;align-items:center;gap:6px}
  .contact-phone svg{width:32px;height:32px}
  .contact-email{top:1213px;font-size:20px;font-weight:400;display:flex;align-items:center;gap:6px}
  .contact-email svg{width:16px;height:16px}
</style>
</head>
<body>
<div class="flyer">
  <div class="hero-photo" role="img" aria-label="Photo of a smiling nurse in scrubs with a stethoscope, medical team in the background"></div>

  <svg class="blue-field" viewBox="0 0 998 1292" aria-hidden="true">
    <defs>
      <radialGradient id="fieldShade" cx="0.55" cy="0.5" r="0.7">
        <stop offset="0" stop-color="#1a5ca3"/>
        <stop offset="1" stop-color="#083263"/>
      </radialGradient>
    </defs>
    <path d="M0,160 C90,250 200,380 380,420 C560,455 760,410 998,410 L998,970 C900,930 820,1010 700,1050 C520,1100 250,1070 0,1082 Z" fill="url(#fieldShade)"/>
    <circle cx="810" cy="986" r="146" fill="#ffffff"/>
  </svg>

  <div class="benefits-card" role="img" aria-label="Sample Medicare benefits card with beneficiary name, claim number and coverage dates"></div>

  <h1 class="headline">The <strong>Value of Working</strong><br>With An <strong>Insurance Agent</strong></h1>

  <ul class="checklist left">
    <li><svg viewBox="0 0 24 24"><circle cx="11" cy="13" r="9" fill="none" stroke="var(--tick)" stroke-width="2.2"/><path d="M6 12 l4 4 l11 -12" fill="none" stroke="var(--tick)" stroke-width="3" stroke-linecap="round"/></svg>MAPD plans offer a personal case manager for their patients when they leave the Skilled Nursing Home.</li>
    <li><svg viewBox="0 0 24 24"><circle cx="11" cy="13" r="9" fill="none" stroke="var(--tick)" stroke-width="2.2"/><path d="M6 12 l4 4 l11 -12" fill="none" stroke="var(--tick)" stroke-width="3" stroke-linecap="round"/></svg>Medicare only clients can get upgraded benefits with an MAPD plan</li>
    <li><svg viewBox="0 0 24 24"><circle cx="11" cy="13" r="9" fill="none" stroke="var(--tick)" stroke-width="2.2"/><path d="M6 12 l4 4 l11 -12" fill="none" stroke="var(--tick)" stroke-width="3" stroke-linecap="round"/></svg>MAPD plans come with CareBeacon to help lower-income Medicare patients get help through 2,000 different community assistant programs.</li>
  </ul>

  <ul class="checklist right">
    <li><svg viewBox="0 0 24 24"><circle cx="11" cy="13" r="9" fill="none" stroke="var(--tick)" stroke-width="2.2"/><path d="M6 12 l4 4 l11 -12" fill="none" stroke="var(--tick)" stroke-width="3" stroke-linecap="round"/></svg>All paperwork is handled by the agent. Usually done in 30 mins and patients plans start the very next month.</li>
    <li><svg viewBox="0 0 24 24"><circle cx="11" cy="13" r="9" fill="none" stroke="var(--tick)" stroke-width="2.2"/><path d="M6 12 l4 4 l11 -12" fill="none" stroke="var(--tick)" stroke-width="3" stroke-linecap="round"/></svg>All Medicare patients entering a Skilled Nursing Center are eligible to make any changes needed to their Medicare benefits upon entering the Skilled Nursing Facility.</li>
    <li><svg viewBox="0 0 24 24"><circle cx="11" cy="13" r="9" fill="none" stroke="var(--tick)" stroke-width="2.2"/><path d="M6 12 l4 4 l11 -12" fill="none" stroke="var(--tick)" stroke-width="3" stroke-linecap="round"/></svg>Services provided by me are no cost to both the Nursing Home and the patient.</li>
  </ul>

  <div class="section-bar"></div>
  <h2 class="section-title">PATIENT BENEFITS</h2>
  <div class="section-cap"></div>
  <p class="benefits-intro">Patients Benefits included in our MAPD plans:</p>

  <ul class="benefit-list left">
    <li>24hr Nurse Hotline</li>
    <li>$200 per year credit for<br>Over-the-Counter items</li>
    <li>Chiropractic and<br>Acupuncture Coverage</li>
  </ul>
  <ul class="benefit-list right">
    <li>$0 copay Eye Exams</li>
    <li>2 Dental Cleanings per year</li>
    <li>Virtual Doctor Visits</li>
    <li>House Call Coverage</li>
    <li>$0 monthly premium</li>
  </ul>

  <div class="agent-portrait" role="img" aria-label="Portrait photo of agent Brent Valdecour"></div>

  <div class="partner-name" style="left:68px;top:1138px;font-size:21px">LWBQ Medicare Harbor</div>
  <div class="partner-name" style="left:142px;top:1166px;font-size:14px;font-weight:500">Northvale Health</div>
  <div class="partner-name" style="left:390px;top:1150px;font-size:17px">Golden Horizons</div>
  <div class="partner-name" style="left:438px;top:1174px;font-size:11px;font-weight:500">Northvale Health</div>
  <div class="partner-rule"></div>
  <div class="partner-row">
    <span class="partner"><span class="dot"></span>Crestway Medical</span>
    <span class="partner"><span class="dot"></span>CareBeacon</span>
    <span class="partner"><span class="dot"></span>Riverline Transit</span>
    <span class="partner"><span class="dot"></span>Vistacall</span>
  </div>

  <div class="contact contact-name">Brent Valdecour</div>
  <div class="contact contact-phone">
    <svg viewBox="0 0 32 32" aria-hidden="true"><circle cx="16" cy="16" r="14" fill="none" stroke="var(--cyan)" stroke-width="2"/><path d="M11 9 l3 0 l1.5 4 l-2 1.5 c1 2.3 2.7 4 5 5 l1.5 -2 l4 1.5 l0 3 c-8 1 -14 -5 -13 -13z" fill="var(--cyan)"/></svg>
    (702)555-0187
  </div>
  <div class="contact contact-email">
    <svg viewBox="0 0 16 16" aria-hidden="true"><circle cx="8" cy="8" r="7" fill="none" stroke="var(--cyan)" stroke-width="1.2"/><rect x="4" y="5.5" width="8" height="5" fill="none" stroke="var(--cyan)" stroke-width="1"/><path d="M4 5.5 l4 3 l4 -3" fill="none" stroke="var(--cyan)" stroke-width="1"/></svg>
    b.valdecour@pinemarkcover.example
  </div>
</div>
</body>
</html>
```